Full Service Outdoor Property Management Company

We are looking for a new and fresh business card design. My company has been in business for 26 years. Winter: We are a large snow and ice management company that does work for commercial, industrial and municipal clients. We have been named "Top 100 Snow Companies in the U.S." for numerous years. Summer: We provide complete landscape maintenance and landscape design and construction for both residential and commercial clients. We must incorporate our logo into card design as well as (in no particular order):
Employees name
Office: (555) 847-2036
Cell: (xxx) xxx-xxxx
thornvale.com
1837 Wrenfield, Alderbrook MI 48139
(Something about 26 + years in business as well as "Top 100 snow contractors as stated above)
Target Market(s)
Winter: Commercial, Industrial, Municipal
Summer: Residential and Commercial
Industry/Entity Type
Construction
Contact Information for Business Card
This is a little challenging as we are using one card for essentially two companies that target different customers from summer to winter. Perhaps the back side could be split in two or something to highlight the different services?? I'm open to any ideas!! Looking forward to seeing what you come up with!
Requirements
Must have
- Logo
- (in no particular order)
- Employees name
- Office: (555) 847-2036
- Cell: (xxx) xxx-xxxx
- thornvale.com
- 1837 Wrenfield, Alderbrook MI 48139
Nice to have
- Something about 26 + years in business
- "Top 100 Snow Contractors in the U.S."
Should not have
- Cheesy pictures of lawn mowers and snow plows

```html
<!DOCTYPE html>
<html lang="en">
<head>
<meta charset="utf-8">
<title>Thornvale Business Card</title>
<link rel="stylesheet" href="https://fonts.googleapis.com/css2?family=Lato:wght@300;400;700;900&display=swap">
<style>
  :root {
    --green-light: #17ad6b;
    --green: #0f9a5c;
    --green-dark: #0a8250;
    --white: #ffffff;
    --paper: #f7f7f5;
    --backdrop: #e8e5df;
    --text-soft: rgba(255,255,255,0.82);
  }
  * { box-sizing: border-box; margin: 0; padding: 0; }
  html, body {
    width: 1200px; height: 1023px; overflow: hidden;
    background: var(--backdrop);
    font-family: "Lato", sans-serif;
  }
  .sheet {
    width: 1200px; height: 1023px;
    display: flex; flex-direction: column; align-items: center; justify-content: center;
    gap: 50px;
  }
  .card {
    position: relative;
    width: 760px; height: 434px;
    background: linear-gradient(135deg, var(--green-light) 0%, var(--green) 45%, var(--green-dark) 100%);
    box-shadow: 0 6px 18px rgba(0,0,0,0.18);
    overflow: hidden;
    color: var(--white);
  }
  .brand-panel {
    position: absolute; top: -1px; right: -1px; bottom: -1px;
    width: 272px;
    background: linear-gradient(180deg, var(--white), var(--paper));
    clip-path: polygon(22% 0, 100% 0, 100% 100%, 22% 100%, 0 50%);
    display: flex; align-items: center; justify-content: center;
    padding-left: 50px;
  }
  .brand-name {
    font-weight: 400;
    font-size: 40px;
    color: var(--green);
    letter-spacing: 0.5px;
  }
  /* front */
  .front-content {
    position: absolute; left: 48px; top: 44px; width: 460px;
  }
  .person-name { font-weight: 900; font-size: 34px; line-height: 1.1; }
  .person-role { font-weight: 300; font-size: 19px; color: var(--text-soft); margin-top: 2px; }
  .address { margin-top: 34px; font-weight: 300; font-size: 19px; line-height: 1.3; }
  .contact-list { list-style: none; margin-top: 8px; font-weight: 300; font-size: 18px; line-height: 1.45; }
  .contact-list li { display: flex; align-items: center; gap: 10px; }
  .contact-icon { width: 15px; height: 15px; flex: none; }
  .credentials { margin-top: 22px; font-weight: 700; font-size: 18px; line-height: 1.45; }
  .credentials .award { font-weight: 900; }
  /* back */
  .back-content {
    position: absolute; left: 48px; top: 52px; width: 460px;
  }
  .season + .season { margin-top: 34px; }
  .season-label {
    display: inline-block;
    background: var(--white);
    color: var(--green-dark);
    font-weight: 900; font-size: 26px;
    padding: 3px 14px 5px;
    border-radius: 9px;
  }
  .season-services { list-style: none; margin-top: 10px; font-weight: 400; font-size: 20px; line-height: 1.35; }
</style>
</head>
<body>
<main class="sheet">
  <section class="card card-front" aria-label="Business card front">
    <div class="front-content">
      <h1 class="person-name">Daniel Reyes</h1>
      <p class="person-role">Director</p>
      <p class="address">1837 Wrenfield, Alderbrook<br>MI 48139</p>
      <ul class="contact-list">
        <li>
          <svg class="contact-icon" viewBox="0 0 16 16" aria-hidden="true"><path d="M3 1h3l1.5 4-2 1.2a9 9 0 0 0 4.3 4.3L11 8.5l4 1.5v3a2 2 0 0 1-2 2C6.9 15 1 9.1 1 3a2 2 0 0 1 2-2z" fill="#fff"/></svg>
          (555) 847-2036
        </li>
        <li>
          <svg class="contact-icon" viewBox="0 0 16 16" aria-hidden="true"><rect x="1.5" y="1.5" width="13" height="13" fill="none" stroke="#fff" stroke-width="1.6"/></svg>
          (xxx) xxx-xxxx
        </li>
        <li>
          <svg class="contact-icon" viewBox="0 0 16 16" aria-hidden="true"><rect x="1.5" y="1.5" width="13" height="13" fill="none" stroke="#fff" stroke-width="1.6"/></svg>
          www.thornvale.com
        </li>
      </ul>
      <p class="credentials">We are 26+ Years in Business<br><span class="award">“Top 100 Snow Companies in the U.S.”</span></p>
    </div>
    <div class="brand-panel"><span class="brand-name">Thornvale</span></div>
  </section>

  <section class="card card-back" aria-label="Business card back">
    <div class="back-content">
      <div class="season season-winter">
        <span class="season-label">Winter:</span>
        <ul class="season-services">
          <li>Large Snow Management Company</li>
          <li>Large Ice Management Company</li>
        </ul>
      </div>
      <div class="season season-summer">
        <span class="season-label">Summer:</span>
        <ul class="season-services">
          <li>Complete Landscape Maintenance</li>
          <li>Landscape Design and Construction</li>
        </ul>
      </div>
    </div>
    <div class="brand-panel"><span class="brand-name">Thornvale</span></div>
  </section>
</main>
</body>
</html>
```